The name of my company is Tolmen Refacing LLC and I would like the sub text to say "Cabinet Refacing and Countertops". Have my name Dorian Tolmen, Owner / Sales, contact info: Cell: 360-555-0147 / Email: dorian.tolmen@quenmail.com

Simple, Clean, and Organized. With colors that will appeal to the eye.

Target Market(s)

Houses and Apartments

Industry/Entity Type

Cabinet Refacing

Contact Information for Business Card

Company name and sub text Dorian Tolmen - Owner / Sales, my cell phone number and email

Requirements
Must have
• Business name, my name / position, and my contact info
Nice to have
• Simple. Organized. Appealing to the eye

```html
<!DOCTYPE html>
<html lang="en">
<head>
<meta charset="utf-8">
<title>Tolmen Refacing LLC – Business Card</title>
<link href="https://fonts.googleapis.com/css2?family=Poppins:wght@300;400;500;600&display=swap" rel="stylesheet">
<style>
  :root {
    --brand-blue: #416cb5;
    --card-white: #ffffff;
    --text-grey: #555a61;
    --backdrop: #2a2a2c;
  }
  * { margin: 0; padding: 0; box-sizing: border-box; }
  html, body {
    width: 1200px; height: 874px; overflow: hidden;
    background: var(--backdrop);
    font-family: "Poppins", sans-serif;
  }
  .sheet {
    width: 1200px; height: 874px;
    display: flex; flex-direction: column;
    align-items: center; justify-content: center; gap: 40px;
  }
  .card {
    width: 640px; height: 366px;
    position: relative; overflow: hidden;
  }
  .card--front {
    background: var(--brand-blue);
    color: var(--card-white);
    display: flex; flex-direction: column;
    align-items: center; justify-content: center;
    text-align: center;
  }
  .company-name {
    font-weight: 300;
    font-size: 34px;
    letter-spacing: 1px;
    text-transform: uppercase;
    line-height: 1.1;
    white-space: nowrap;
  }
  .company-tagline {
    font-weight: 600;
    font-size: 17px;
    margin-top: 10px;
    white-space: nowrap;
  }
  .card--back { background: var(--card-white); }
  .contact-block {
    position: absolute; left: 70px; top: 58px;
  }
  .person-name {
    color: var(--brand-blue);
    font-weight: 500;
    font-size: 24px;
    text-transform: uppercase;
    letter-spacing: 0.5px;
    line-height: 1;
    white-space: nowrap;
  }
  .person-role {
    color: var(--text-grey);
    font-weight: 400;
    font-size: 16px;
    margin-top: 4px;
  }
  .contact-list { list-style: none; margin-top: 18px; }
  .contact-item {
    display: flex; align-items: center; gap: 10px;
    color: var(--text-grey);
    font-size: 16px; line-height: 1.5;
    white-space: nowrap;
  }
  .contact-icon { width: 12px; height: 12px; fill: var(--brand-blue); flex: none; }
</style>
</head>
<body>
  <main class="sheet">
    <section class="card card--front" aria-label="Card front">
      <h1 class="company-name">Tolmen Refacing, LLC</h1>
      <p class="company-tagline">Cabinet Refacing and Countertops</p>
    </section>

    <section class="card card--back" aria-label="Card back">
      <div class="contact-block">
        <h2 class="person-name">Dorian Tolmen</h2>
        <p class="person-role">Owner / Sales</p>
        <ul class="contact-list">
          <li class="contact-item">
            <svg class="contact-icon" viewBox="0 0 24 24" aria-hidden="true"><path d="M6.6 10.8a15.1 15.1 0 0 0 6.6 6.6l2.2-2.2a1 1 0 0 1 1-.25 11.4 11.4 0 0 0 3.6.57 1 1 0 0 1 1 1V20a1 1 0 0 1-1 1A17 17 0 0 1 3 4a1 1 0 0 1 1-1h3.5a1 1 0 0 1 1 1c0 1.25.2 2.45.57 3.57a1 1 0 0 1-.25 1z"/></svg>
            <span>360-555-0147</span>
          </li>
          <li class="contact-item">
            <svg class="contact-icon" viewBox="0 0 24 24" aria-hidden="true"><path d="M2 5h20v14H2z M2 5l10 8 10-8" /></svg>
            <span>dorian.tolmen@quenmail.com</span>
          </li>
        </ul>
      </div>
    </section>
  </main>
</body>
</html>
```